Korvane Development and Management Corp. Business Card

A logo design project has been started for our Calgary-Alberta, Canada based land development and project management company. Using this logo, a clean, sleek, professional business card is to be developed (for digital or print media) representing the principals of the company (community, sustainability, and harmony).
Updates

Reason: Logo design recently completed.

Adobe Illustrator Vector file uploaded. Thanks, Lev

Target Market(s)

Similar business development professionals and other engineering project management personnel involved in land developemtn. Also used to as as the brand and image with both private individuals (Landowners), public officials (policy makers), and investors (banks, venture capitalists).

Industry/Entity Type

Digital

Requirements
Must have
• Open to designers opinion. Based on logo. Must have logo, and space for employee name, title, address, website, office / cell numbers.
Should not have
• No Palm trees or tropical references. Company is based in Calgary, Alberta, Canada.

```html
<!DOCTYPE html>
<html lang="en">
<head>
<meta charset="utf-8">
<title>Korvane Development and Management Corp. Business Card</title>
<link rel="stylesheet" href="https://fonts.googleapis.com/css2?family=Cinzel:wght@400;700&family=Open+Sans:wght@400;700&display=swap">
<style>
  :root {
    --backdrop: #e9e6e1;
    --card-top: #2a2a2a;
    --card-bottom: #0c0c0c;
    --band: #3a3a3a;
    --lime: #b7d23a;
    --grey-text: #b9b9b9;
    --grey-soft: #8a8a8a;
    --deco: #5b5b5b;
  }
  * { box-sizing: border-box; margin: 0; padding: 0; }
  html, body { width: 1200px; height: 1023px; overflow: hidden; }
  body {
    background: var(--backdrop);
    display: flex; align-items: center; justify-content: center;
  }
  .business-card {
    position: relative;
    width: 900px; height: 520px;
    border-radius: 6px;
    background: linear-gradient(160deg, var(--card-top) 0%, #141414 55%, var(--card-bottom) 100%);
    box-shadow: 0 14px 34px rgba(0,0,0,.35);
    overflow: hidden;
    font-family: "Open Sans", Arial, sans-serif;
  }
  .brand {
    position: absolute; left: 70px; top: 62px;
    display: flex; align-items: center; gap: 18px;
  }
  .brand-mark { width: 46px; height: 46px; background: var(--lime); }
  .brand-name {
    font-family: "Cinzel", Georgia, serif;
    font-weight: 700; font-size: 64px; letter-spacing: 2px;
    color: var(--lime); line-height: 1;
  }
  .brand-tagline {
    position: absolute; left: 136px; top: 136px;
    font-size: 17px; color: var(--grey-text);
  }
  .person { position: absolute; left: 70px; top: 198px; }
  .person-name {
    font-family: "Cinzel", Georgia, serif;
    font-size: 27px; color: var(--lime); letter-spacing: 1.5px;
  }
  .person-title { font-size: 17px; color: var(--grey-text); margin-top: 4px; }
  .contact-list { position: absolute; left: 70px; top: 282px; list-style: none; }
  .contact-item {
    display: flex; align-items: center; gap: 12px;
    font-size: 18px; color: var(--grey-text); height: 30px;
  }
  .contact-icon {
    width: 18px; height: 18px; border-radius: 3px;
    background: var(--lime);
    display: flex; align-items: center; justify-content: center;
  }
  .contact-icon svg { width: 12px; height: 12px; }
  .decoration {
    position: absolute; right: 70px; top: 70px;
    width: 300px; height: 300px;
    background: var(--deco); opacity: .55;
  }
  .address-band {
    position: absolute; left: 0; right: 0; bottom: 0; height: 62px;
    background: linear-gradient(180deg, #1a1a1a, var(--band));
    display: flex; align-items: center; padding-left: 70px;
    font-weight: 700; font-size: 20px; color: var(--lime);
    text-transform: uppercase; letter-spacing: .5px;
  }
</style>
</head>
<body>
  <article class="business-card">
    <div class="brand">
      <span class="brand-mark"></span>
      <span class="brand-name">KORVANE</span>
    </div>
    <p class="brand-tagline">Development and Management Corp</p>

    <div class="person">
      <p class="person-name">MARCO BELLANDI</p>
      <p class="person-title">Director</p>
    </div>

    <ul class="contact-list">
      <li class="contact-item">
        <span class="contact-icon"><svg viewBox="0 0 12 12"><rect x="3" y="1" width="6" height="10" rx="1" fill="#111"/></svg></span>
        403-555-0172
      </li>
      <li class="contact-item">
        <span class="contact-icon"><svg viewBox="0 0 12 12"><path d="M2 1h3l1 3-2 1a7 7 0 0 0 3 3l1-2 3 1v3c-6 0-9-3-9-9z" fill="#111"/></svg></span>
        403-555-0936
      </li>
      <li class="contact-item">
        <span class="contact-icon"><svg viewBox="0 0 12 12"><rect x="1" y="3" width="10" height="7" fill="#111"/><path d="M1 3l5 4 5-4" stroke="#b7d23a" fill="none"/></svg></span>
        marco@korvane.com
      </li>
      <li class="contact-item">
        <span class="contact-icon"><svg viewBox="0 0 12 12"><circle cx="6" cy="6" r="4.5" fill="none" stroke="#111" stroke-width="1.4"/><path d="M1.5 6h9M6 1.5v9" stroke="#111"/></svg></span>
        www.korvane.com
      </li>
    </ul>

    <div class="decoration" role="img" aria-label="Large faint brand mark decoration"></div>

    <div class="address-band">214 Birchwood Ave SW, Calgary, Alberta</div>
  </article>
</body>
</html>
```